QRV Law Letterhead

Want law firm letterhead - both in terms of a pdf file that I can use electronically as letterhead by adding it as a background - and in terms of a file that I can send to a company to create actual letterhead.
Industry/Entity Type
Law Firm
Font styles to use
Sans Serif
Requirements
Must have
- Should have the following information (you can decide where to place):
- My name - Corwin Haldane
- My email - corwin@qrvlawfirm.example
- My address - 2816 Pellworth Parkway 317-842
- San Jose, California 95742
- Website - www.qrvlawfirm.example
- Phone - 408-555-0187
- Fax - 408-555-0243
- The logo I attached
Nice to have
- I think I would prefer to have a black and white color scheme.
- I don't necessarily need a title after my name, but I have seen a few design submissions that include a generic title. The title I would use is "IP Litigator & Trademark Attorney"

```html
<!DOCTYPE html>
<html lang="en">
<head>
<meta charset="utf-8">
<title>QRV Law Letterhead</title>
<link rel="stylesheet" href="https://fonts.googleapis.com/css2?family=Barlow:wght@400;500;600&display=swap">
<style>
  :root {
    --backdrop: #e6e6e6;
    --paper: #ffffff;
    --ink: #1a1a1a;
    --rule: #8a8a8a;
  }
  * { margin: 0; padding: 0; box-sizing: border-box; }
  html, body {
    width: 1200px;
    height: 1200px;
    overflow: hidden;
    background: var(--backdrop);
    font-family: "Barlow", Arial, sans-serif;
    color: var(--ink);
  }
  .letterhead {
    position: absolute;
    left: 199px;
    top: 33px;
    width: 802px;
    height: 1133px;
    background: var(--paper);
  }
  .brand {
    position: absolute;
    top: 84px;
    left: 0;
    width: 100%;
    display: flex;
    justify-content: center;
    align-items: center;
    gap: 14px;
  }
  .brand-dot {
    width: 44px;
    height: 44px;
    border-radius: 50%;
    background: var(--ink);
  }
  .brand-name {
    font-size: 48px;
    font-weight: 500;
    letter-spacing: 0.5px;
    line-height: 1;
  }
  .signatory {
    position: absolute;
    top: 173px;
    left: 0;
    width: 100%;
    display: flex;
    justify-content: center;
    align-items: center;
    gap: 10px;
  }
  .signatory-rule {
    width: 103px;
    height: 1px;
    background: var(--ink);
    margin-top: 4px;
  }
  .signatory-text { text-align: left; }
  .signatory-name {
    font-size: 15px;
    font-weight: 600;
    line-height: 1.1;
    letter-spacing: 0.3px;
  }
  .signatory-title {
    font-size: 8.5px;
    font-weight: 400;
    line-height: 1.1;
  }
  .contact {
    position: absolute;
    top: 1046px;
    left: 0;
    width: 100%;
  }
  .contact-rule {
    position: absolute;
    top: 28px;
    height: 1px;
    background: var(--rule);
  }
  .contact-rule.left { left: 0; width: 179px; }
  .contact-rule.right { left: 624px; right: 0; }
  .contact-bar {
    position: absolute;
    top: 4px;
    width: 1px;
    height: 48px;
    background: var(--rule);
  }
  .contact-bar.left { left: 179px; }
  .contact-bar.right { left: 624px; }
  .contact-lines {
    position: absolute;
    left: 179px;
    width: 445px;
    text-align: center;
    font-size: 15.5px;
    font-weight: 500;
    line-height: 19px;
  }
  .sep { padding: 0 6px; }
</style>
</head>
<body>
  <main class="letterhead">
    <header class="brand">
      <span class="brand-dot"></span>
      <span class="brand-name">QRV Law</span>
    </header>

    <section class="signatory">
      <span class="signatory-rule"></span>
      <div class="signatory-text">
        <div class="signatory-name">Corwin HALDANE</div>
        <div class="signatory-title">IP Litigator &amp; Trademark Attorney</div>
      </div>
      <span class="signatory-rule"></span>
    </section>

    <footer class="contact">
      <span class="contact-rule left"></span>
      <span class="contact-bar left"></span>
      <div class="contact-lines">
        <div>2816 Pellworth Parkway 317-842 San Jose, California 95742</div>
        <div>www.qrvlawfirm.example<span class="sep">|</span>corwin@qrvlawfirm.example</div>
        <div>Phone: 408-555-0187<span class="sep">|</span>Fax: 408-555-0243</div>
      </div>
      <span class="contact-bar right"></span>
      <span class="contact-rule right"></span>
    </footer>
  </main>
</body>
</html>
```